Stationary & Business Card for Talvo Co, LLC
Talvo Co, LLC
Professional
Adrian Pellworth, MD
President
2918 Larkfield Ave., Suite C-240
Bethesda, MD 20846
dradrian@talvocollc.com
www.talvocollc.com
Our tagline is Your Partner in Personalized Healthcare.
We would like a solid color for our back - either matching the purple or gold of our logo

```html
<!DOCTYPE html>
<html lang="en">
<head>
<meta charset="utf-8">
<title>Talvo Co, LLC — Business Card</title>
<link rel="stylesheet" href="https://fonts.googleapis.com/css2?family=Lato:wght@400;700;900&display=swap">
<style>
  :root {
    --purple: #4b2a6b;
    --gold: #b8923a;
    --ink: #3d3d45;
    --muted: #7a7a84;
    --card: #ffffff;
    --stage: #ecebef;
  }
  * { box-sizing: border-box; margin: 0; padding: 0; }
  html, body { width: 1200px; height: 629px; overflow: hidden; }
  body {
    background: var(--stage);
    font-family: "Lato", Arial, sans-serif;
    position: relative;
  }
  .card {
    position: absolute;
    width: 520px;
    height: 297px;
    background: var(--card);
    box-shadow: 0 6px 18px rgba(40, 30, 60, 0.18);
    overflow: hidden;
  }
  .card--back { left: 50px; top: 166px; }
  .card--front { left: 630px; top: 166px; }

  .brand { display: flex; align-items: center; gap: 12px; }
  .brand__dot {
    width: 44px; height: 44px; border-radius: 50%;
    background: var(--purple); flex: none;
  }
  .brand__name {
    font-weight: 900; color: var(--purple);
    font-size: 30px; letter-spacing: 0.5px; white-space: nowrap;
  }
  .brand__tagline {
    font-size: 9px; letter-spacing: 1.2px; color: var(--gold);
    text-transform: uppercase; margin-top: 4px;
  }

  .card--back .brand-block {
    position: absolute; left: 0; right: 0; top: 112px;
    display: flex; flex-direction: column; align-items: center;
  }

  .card--front .brand-block { position: absolute; left: 32px; top: 38px; }
  .card--front .brand__dot { width: 32px; height: 32px; }
  .card--front .brand__name { font-size: 22px; }
  .card--front .brand__tagline { font-size: 7px; margin-left: 44px; }

  .person { position: absolute; right: 34px; top: 48px; text-align: right; }
  .person__name { font-size: 15px; font-weight: 700; color: var(--purple); }
  .person__title { font-size: 11px; color: var(--muted); margin-top: 3px; }

  .contact { position: absolute; left: 32px; bottom: 26px; list-style: none; }
  .contact__item {
    display: flex; align-items: center; gap: 8px;
    font-size: 9.5px; color: var(--ink); line-height: 17px;
  }
  .contact__icon { width: 11px; height: 11px; flex: none; }

  .accent-bar {
    position: absolute; right: 0; bottom: 0;
    width: 210px; height: 12px; background: var(--purple);
  }
</style>
</head>
<body>

<section class="card card--back" aria-label="Business card back">
  <div class="brand-block">
    <div class="brand">
      <span class="brand__dot"></span>
      <span class="brand__name">Talvo Co, LLC</span>
    </div>
    <p class="brand__tagline">Your Partner in Personalized Healthcare</p>
  </div>
</section>

<section class="card card--front" aria-label="Business card front">
  <div class="brand-block">
    <div class="brand">
      <span class="brand__dot"></span>
      <span class="brand__name">Talvo Co, LLC</span>
    </div>
    <p class="brand__tagline">Your Partner in Personalized Healthcare</p>
  </div>

  <div class="person">
    <p class="person__name">Adrian Pellworth, MD</p>
    <p class="person__title">President</p>
  </div>

  <ul class="contact">
    <li class="contact__item">
      <svg class="contact__icon" viewBox="0 0 12 12"><circle cx="6" cy="6" r="6" fill="#4b2a6b"/><path d="M6 2.6a2.2 2.2 0 0 0-2.2 2.2C3.8 6.5 6 9.4 6 9.4s2.2-2.9 2.2-4.6A2.2 2.2 0 0 0 6 2.6z" fill="#fff"/></svg>
      2918 Larkfield Ave., Suite C-240
    </li>
    <li class="contact__item">
      <svg class="contact__icon" viewBox="0 0 12 12"><circle cx="6" cy="6" r="6" fill="#4b2a6b"/><circle cx="6" cy="6" r="1.6" fill="#fff"/></svg>
      Bethesda, MD 20846
    </li>
    <li class="contact__item">
      <svg class="contact__icon" viewBox="0 0 12 12"><circle cx="6" cy="6" r="6" fill="#4b2a6b"/><path d="M4 3h1.3l.6 1.6-.8.6a4 4 0 0 0 1.7 1.7l.6-.8L9 6.7V8a1 1 0 0 1-1 1A5 5 0 0 1 3 4a1 1 0 0 1 1-1z" fill="#fff"/></svg>
      (301) 555-0142
    </li>
    <li class="contact__item">
      <svg class="contact__icon" viewBox="0 0 12 12"><circle cx="6" cy="6" r="6" fill="#4b2a6b"/><rect x="3" y="4" width="6" height="4.2" fill="#fff"/><path d="M3 4l3 2.3L9 4" stroke="#4b2a6b" stroke-width=".7" fill="none"/></svg>
      dradrian@talvocollc.com
    </li>
    <li class="contact__item">
      <svg class="contact__icon" viewBox="0 0 12 12"><circle cx="6" cy="6" r="6" fill="#4b2a6b"/><circle cx="6" cy="6" r="3" stroke="#fff" stroke-width=".8" fill="none"/><path d="M3 6h6M6 3v6" stroke="#fff" stroke-width=".6"/></svg>
      www.talvocollc.com
    </li>
    <li class="contact__item">
      <svg class="contact__icon" viewBox="0 0 12 12"><circle cx="6" cy="6" r="6" fill="#4b2a6b"/></svg>
      talvocollc
    </li>
  </ul>

  <div class="accent-bar"></div>
</section>

</body>
</html>
```